Brochure Design Project

I am looking for a trifold brochure.
I would like it to be square (5.5 x 5.5)
The back needs to be reserved for a map and logo information.

we are a financial planning firm. we have been in operation for 15 years.
our clients are ecstatic and continue to refer others to us.

Brochure COPY:
Building Wealth, Building Futures
We start with your goals. Then we build a comprehensive strategy to manage your investments, grow your wealth, minimize your tax burden and protect your family. Most importantly, we keep you informed about market change, opportunities and concerns before they impact you, so you can make confident decisions about your future, every step of the way.

Understanding and Expertise (bios)
Steadfast Money Partners is led by Lorna Feldskov and Miriam Oakhurst, experienced business partners who take the time to listen to you, understand your needs and present you with all your options.
Our focus in on your future, and building a confident and financially secure path for you and your family for the years ahead.

Lorna Feldskov, BSc, MBA, CPA, CA, CFP, FMA, CPCA
Certified Financial Planner

With years of experience in tax, investment, estate and retirement issues - and an extensive business background - Lorna provided her clients with important financial insights and clear direction in a friendly and open manner.

Miriam Oakhurst, BSEd, FMA, CPCA, CFP, FCSI, CIM

After a successful tennis career Miriam joined Lorna in the financial industry. Miriam quickly discovered how much she enjoys working with people and helping them to achieve their goals. Leveraging the discipline and work ethic developed during her tennis career, Miriam has been instrumental in creating the successful process used by Steadfast Money Partners.

People Trust Us to Help Them
The important things in life are often neglected due to the demands of day to day, including financial planning and wealth management. But it doesn't have to be that way when you have a trustworthy team looking out for you.
At Steadfast Money Partners we have the knowledge, experience and resources to help you move forward and realize your financial goals.

(side note) on the back of the brochure it should have the SMP logo, the office address, 382 Kettlewood Rd. E. Mississauga, ON L5R 7M4, and our website address.

Reason: Am juggling a number of different projects so need to extend the deadline on this one. Will provide copy for the project by end of day today.

Target Market(s)

We would like the brochure to appeal to the high net worth client who is currently working with an advisor but is not getting the attention from them.

Industry/Entity Type

Financial

Requirements
Must have
• SMP Logo on the front. The logo is blue with black font and has a tagline with it that says "Choose your path, change your future."
you can see the logo at www.plantharvestsoon.ca

One page must be about the two advisors, Lorna Feldskov and Miriam Oakhurst.
(leave an open area for bios and we will fill it in)

We want it to talk about building wealth and passing it on to the next generation.
Should not have
• Financial lingo.

```html
<!DOCTYPE html>
<html lang="en">
<head>
<meta charset="utf-8">
<title>Steadfast Money Partners – Trifold Brochure</title>
<link href="https://fonts.googleapis.com/css2?family=Open+Sans:wght@400;600;700&family=Roboto+Condensed:wght@700&display=swap" rel="stylesheet">
<style>
:root{
  --blue:#1c5aa8;
  --navy:#26304f;
  --ink:#1d1d1f;
  --grey-text:#444a55;
  --paper:#ffffff;
  --paper-soft:#f1f3f6;
  --tint:#e4edf8;
  --stage:#7f8186;
}
*{box-sizing:border-box;margin:0;padding:0}
html,body{width:1200px;height:900px;overflow:hidden}
body{background:var(--stage);font-family:"Open Sans",Arial,sans-serif;color:var(--grey-text);position:relative}
.sheet{position:absolute;left:30px;width:1140px;height:380px;display:flex;box-shadow:0 6px 18px rgba(0,0,0,.3)}
.sheet--outside{top:50px}
.sheet--inside{top:470px}
.panel{position:relative;width:380px;height:380px;overflow:hidden;background:linear-gradient(180deg,var(--paper) 0%,var(--paper-soft) 100%)}
.panel+.panel{border-left:1px solid #d9dde3}

/* brand lockup */
.brand{position:absolute;display:flex;flex-direction:column;align-items:flex-start}
.brand__row{display:flex;align-items:center;gap:8px}
.brand__dot{width:14px;height:14px;border-radius:50%;background:var(--blue)}
.brand__name{font-size:17px;font-weight:400;color:var(--ink);letter-spacing:.2px}
.brand__tagline{font-size:10px;color:var(--blue);margin-top:3px;margin-left:22px}

/* trust panel */
.trust__band{position:absolute;inset:0}
.trust__title{position:absolute;left:22px;top:22px;font-family:"Roboto Condensed",Arial,sans-serif;font-size:30px;line-height:30px;color:#fff;text-transform:uppercase}
.trust__art{position:absolute;left:18px;top:180px;width:140px;height:100px;border-radius:4px;background:linear-gradient(135deg,var(--navy),#5b78b6)}
.trust__copy{position:absolute;left:175px;top:172px;width:185px;font-size:9.5px;line-height:1.5;color:var(--grey-text)}
.trust__copy p+p{margin-top:8px}

/* back panel */
.back__title{position:absolute;left:34px;top:28px;font-size:12px;color:var(--ink);text-decoration:underline}
.back__map{position:absolute;left:34px;top:50px;width:312px;height:150px;border:1px solid #b9bec6;background:linear-gradient(135deg,#e9ecdf,#d6dccb)}
.back .brand{left:34px;top:232px}
.back__rule{position:absolute;left:34px;top:282px;width:312px;height:1px;background:#c9ced6}
.back__contact{position:absolute;left:34px;top:294px;font-size:11px;line-height:1.7;color:var(--ink);font-style:normal}

/* cover */
.cover .brand{left:36px;top:40px}
.cover__photo{position:absolute;left:20px;top:110px;width:150px;height:260px;border-radius:6px;background:linear-gradient(160deg,#e7dcc4 0%,#b0935a 50%,#7a6238 100%)}
.cover__headline{position:absolute;left:182px;top:228px;font-family:"Roboto Condensed",Arial,sans-serif;font-size:23px;line-height:24px;color:var(--ink);text-transform:uppercase;letter-spacing:-.2px;white-space:nowrap}
.cover__headline .accent{color:var(--blue)}

/* approach panel */
.approach__photo{position:absolute;left:0;top:150px;width:170px;height:230px;background:linear-gradient(160deg,#f2d6c4,#d9ab92)}
.approach__card{position:absolute;left:110px;top:60px;width:250px;padding:16px 18px;background:#e3e6ea;border-radius:3px;box-shadow:0 2px 6px rgba(0,0,0,.15);font-size:10px;line-height:1.55;color:var(--ink)}

/* about panel */
.about__art{position:absolute;left:24px;top:34px;width:140px;height:150px;border-radius:6px;background:linear-gradient(160deg,var(--tint),#b9cde8)}
.about__title{position:absolute;left:176px;top:80px;font-family:"Roboto Condensed",Arial,sans-serif;font-size:23px;line-height:24px;color:var(--blue)}
.about__title small{display:block;font-family:"Open Sans",Arial,sans-serif;font-weight:400;font-size:11px;line-height:16px;color:var(--navy)}
.about__copy{position:absolute;left:30px;top:206px;width:320px;font-size:10px;line-height:1.55;color:var(--ink)}
.about__copy p+p{margin-top:8px}

/* bios panel */
.bios{background:var(--blue)}
.bio{position:absolute;left:22px;width:336px;display:flex;gap:12px;color:#fff}
.bio--first{top:24px}
.bio--second{top:200px}
.bio__photo{flex:0 0 52px;height:52px;border-radius:8px;background:#e6e9ee}
.bio__name{font-family:"Roboto Condensed",Arial,sans-serif;font-size:17px;line-height:19px}
.bio__creds{font-size:8.5px;font-weight:700;margin-top:2px}
.bio__role{font-size:8.5px;font-weight:700;margin-bottom:5px}
.bio__text{font-size:8.5px;line-height:1.5;opacity:.95}
</style>
</head>
<body>

<section class="sheet sheet--outside" aria-label="Outside of brochure">
  <article class="panel trust">
    <svg class="trust__band" width="380" height="380" viewBox="0 0 380 380" aria-hidden="true">
      <rect width="380" height="380" fill="var(--tint)"/>
      <polygon points="0,0 380,0 380,110 0,200" fill="var(--blue)"/>
    </svg>
    <h2 class="trust__title">People<br>trust us<br>to help them</h2>
    <div class="trust__art" role="img" aria-label="Illustration of two hands in a handshake"></div>
    <div class="trust__copy">
      <p>The important things in life are often neglected due to the demands of day to day, including financial planning and wealth management. But it doesn't have to be that way when you have a trustworthy team looking out for you.</p>
      <p>At Steadfast Money Partners we have the knowledge, experience and resources to help you move forward and realize your financial goals.</p>
    </div>
  </article>

  <article class="panel back">
    <h3 class="back__title">Location Plan</h3>
    <div class="back__map" role="img" aria-label="Street map showing the office location"></div>
    <div class="brand">
      <div class="brand__row"><span class="brand__dot"></span><span class="brand__name">Steadfast Money Partners</span></div>
      <span class="brand__tagline">Choose your path, change your future.</span>
    </div>
    <div class="back__rule"></div>
    <address class="back__contact">
      382 Kettlewood Rd. E. Mississauga, ON L5R 7M4<br>
      www.plantharvestsoon.ca
    </address>
  </article>

  <article class="panel cover">
    <div class="brand">
      <div class="brand__row"><span class="brand__dot"></span><span class="brand__name">Steadfast Money Partners</span></div>
      <span class="brand__tagline">Choose your path, change your future.</span>
    </div>
    <div class="cover__photo" role="img" aria-label="Photograph of an antique brass key with a pocket watch"></div>
    <h1 class="cover__headline">Building <span class="accent">Wealth.</span><br><span class="accent">Building</span> Futures.</h1>
  </article>
</section>

<section class="sheet sheet--inside" aria-label="Inside of brochure">
  <article class="panel approach">
    <div class="approach__photo" role="img" aria-label="Photograph of a hand holding a card"></div>
    <p class="approach__card">We start with your goals. Then we build a comprehensive strategy to manage your investments, grow your wealth, minimize your tax burden and protect your family. Most importantly, we keep you informed about market change, opportunities and concerns before they impact you, so you can make confident decisions about your future, every step of the way.</p>
  </article>

  <article class="panel about">
    <div class="about__art" role="img" aria-label="Line illustration of a head in profile"></div>
    <h2 class="about__title">Understanding<br>and Expertise<small>(bios)</small></h2>
    <div class="about__copy">
      <p>Steadfast Money Partners is led by Lorna Feldskov and Miriam Oakhurst, experienced business partners who take the time to listen to you, understand your needs and present you with all your options.</p>
      <p>Our focus is on your future, and building a confident and financially secure path for you and your family for the years ahead.</p>
    </div>
  </article>

  <article class="panel bios">
    <div class="bio bio--first">
      <div class="bio__photo" role="img" aria-label="Portrait of Lorna Feldskov"></div>
      <div>
        <h3 class="bio__name">Lorna Feldskov</h3>
        <p class="bio__creds">BSc, MBA, CPA, CA, CFP, FMA, CPCA</p>
        <p class="bio__role">Certified Financial Planner</p>
        <p class="bio__text">With years of experience in tax, investment, estate and retirement issues – and an extensive business background – Lorna provides her clients with important financial insights and clear direction in a friendly and open manner.</p>
      </div>
    </div>
    <div class="bio bio--second">
      <div class="bio__photo" role="img" aria-label="Portrait of Miriam Oakhurst"></div>
      <div>
        <h3 class="bio__name">Miriam Oakhurst</h3>
        <p class="bio__creds">BSEd, FMA, CPCA, CFP, FCSI, CIM</p>
        <p class="bio__role">Certified Financial Planner</p>
        <p class="bio__text">After a successful tennis career Miriam joined Lorna in the financial industry. Miriam quickly discovered how much she enjoys working with people and helping them to achieve their goals. Leveraging the discipline and work ethic developed during her tennis career, Miriam has been instrumental in creating the successful process used by Steadfast Money Partners.</p>
      </div>
    </div>
  </article>
</section>

</body>
</html>
```